Lone Elm Cattle Website

I need a website for my cattle company. I will be sharing pictures of my herd along with selling my calves individually. I need the following pages:
About
Cattle Sales
Bulls
Cows/Heifers
Gallery
Contact Us

I just uploaded a few pictures, but I have a lot more!

```html
<!DOCTYPE html>
<html lang="en">
<head>
<meta charset="utf-8">
<title>Lone Elm Cattle</title>
<link href="https://fonts.googleapis.com/css2?family=Montserrat:wght@400;500;600&display=swap" rel="stylesheet">
<style>
:root{
  --cream:#f3efe8;
  --brown:#5b4229;
  --brown-dark:#4a3722;
  --footer:#55422c;
  --tan:#8a7157;
  --text:#5a4a3c;
  --white:#ffffff;
  --btn:#ece9e4;
}
*{margin:0;padding:0;box-sizing:border-box}
html,body{width:1200px;height:2748px;overflow:hidden}
body{font-family:"Montserrat",sans-serif;background:var(--white);color:var(--text);position:relative}
.abs{position:absolute}
/* header */
.site-header{top:0;left:0;width:1200px;height:86px;background:var(--cream);z-index:2}
.brand-badge{left:72px;top:-12px;width:164px;height:160px;border-radius:50%;background:var(--cream);z-index:3;display:flex;align-items:center;justify-content:center;flex-direction:column}
.brand-badge .name{font-weight:600;color:var(--brown);font-size:17px;text-align:center;line-height:1.2;margin-top:8px}
.nav a{position:absolute;top:32px;font-size:15.5px;color:var(--text);text-decoration:none}
.nav a.active{color:var(--brown);font-weight:600}
.nav a.active::after{content:"";position:absolute;left:0;right:0;bottom:-8px;height:2px;background:var(--brown)}
.icons svg{position:absolute;top:32px}
/* hero */
.hero-left{top:86px;left:0;width:546px;height:472px;background:linear-gradient(120deg,#4f3a23,#5a4328 60%,#4a3621)}
.hero-photo{top:86px;left:546px;width:654px;height:472px;background:linear-gradient(180deg,#9aa56a 0%,#7e8750 45%,#5f6a3c 100%)}
.eyebrow-light{left:111px;top:197px;color:var(--white);font-size:17px}
.hero-title{left:111px;top:226px;color:var(--white);font-weight:600;font-size:45px;line-height:51px}
.btn{display:flex;align-items:center;justify-content:center;background:var(--btn);color:var(--text);font-size:15.5px;width:143px;height:37px}
.hero-btn{left:111px;top:413px}
.slider-arrows{left:384px;top:498px;width:226px;height:60px;background:var(--tan);display:flex;align-items:center}
.slider-arrows span{flex:1;display:flex;justify-content:center}
.slider-arrows i{width:1px;height:38px;background:rgba(255,255,255,.7)}
/* about */
.about-img{left:75px;top:715px;width:501px;height:320px;border-radius:50% 50% 6% 6%/70% 70% 8% 8%;background:linear-gradient(180deg,#ebe9e6 0%,#c88a52 55%,#7a8f3e 100%)}
.eyebrow{font-size:17px;color:var(--text)}
.heading{font-weight:600;color:var(--brown);font-size:45px;line-height:51px}
.about-eyebrow{left:608px;top:642px}
.about-heading{left:608px;top:671px}
.about-text{left:608px;top:800px;width:490px;font-size:15.4px;line-height:25.7px}
.about-btn{left:608px;top:1072px}
/* provide */
.provide{top:1191px;left:0;width:1200px;height:660px;background:linear-gradient(180deg,#efe7da 0%,#d8d2bd 25%,#b9b58f 55%,#9d9a6e 100%)}
.provide-edge{top:1800px;left:0}
.center{left:0;width:1200px;text-align:center}
.card{top:1399px;width:305px;height:288px;border-radius:16px}
.pill{top:1661px;width:240px;height:52px;border-radius:14px;background:var(--white);display:flex;align-items:center;justify-content:center;font-size:21px;font-weight:500;color:var(--text);box-shadow:0 4px 10px rgba(0,0,0,.12)}
/* testimonials */
.avatar{left:536px;top:2051px;width:128px;height:128px;border-radius:50%;background:linear-gradient(180deg,#e9b892,#c98a62 60%,#2f3540)}
.quote-text{left:245px;top:2206px;width:710px;text-align:center;font-size:15.4px;line-height:26px}
.client-name{top:2303px;font-size:18.5px;font-weight:600;color:#1f1a15}
.client-role{top:2330px;font-size:16.5px;color:var(--brown)}
.dots{top:2389px;left:495px;display:flex;gap:10px}
.dots i{width:46px;height:4px;border:1px solid var(--tan);display:block}
.dots i.on{background:var(--brown-dark);border-color:var(--brown-dark)}
/* footer */
.site-footer{top:2477px;left:0;width:1200px;height:271px;background:var(--footer)}
.footer-brand{top:2560px;font-size:21px;font-weight:600;color:var(--white)}
.footer-nav{top:2653px;display:flex;justify-content:center;gap:46px;font-size:18px;color:var(--white)}
.footer-rule{top:2702px;left:0;width:1200px;height:1px;background:rgba(255,255,255,.35)}
.copyright{top:2714px;font-size:13px;color:var(--white)}
</style>
</head>
<body>
<header class="abs site-header">
  <nav class="nav">
    <a class="active" style="left:299px">Home</a>
    <a style="left:387px">About Us</a>
    <a style="left:499px">Cattle Sales</a>
    <a style="left:629px">Bulls</a>
    <a style="left:707px">Cows</a>
    <a style="left:789px">Gallery</a>
    <a style="left:883px">Contact Us</a>
  </nav>
  <div class="icons">
    <svg style="left:1001px" width="20" height="20" viewBox="0 0 20 20"><circle cx="8" cy="8" r="6" fill="none" stroke="#2b2118" stroke-width="2.4"/><path d="M12.5 12.5L18 18" stroke="#2b2118" stroke-width="2.6"/></svg>
    <svg style="left:1035px" width="20" height="20" viewBox="0 0 20 20"><path d="M1 2h3l2.5 10h10L19 5H6" fill="#2b2118" stroke="#2b2118" stroke-width="1.5"/><circle cx="8" cy="16" r="1.8" fill="#2b2118"/><circle cx="15" cy="16" r="1.8" fill="#2b2118"/></svg>
    <svg style="left:1069px" width="18" height="20" viewBox="0 0 18 20"><circle cx="9" cy="5.5" r="4.5" fill="#2b2118"/><path d="M1 19c0-5 3.5-8 8-8s8 3 8 8z" fill="#2b2118"/></svg>
  </div>
</header>
<div class="abs brand-badge"><div class="name">Lone Elm<br>Cattle</div></div>

<section>
  <div class="abs hero-left"></div>
  <div class="abs hero-photo" role="img" aria-label="Highland bull standing in tall grass beside a pond"></div>
  <p class="abs eyebrow-light">Welcome To Lone-Elm-Cattle</p>
  <h1 class="abs hero-title">Quality Cattle,<br>Trusted for<br>Generations</h1>
  <a class="abs btn hero-btn">Explore More</a>
  <div class="abs slider-arrows">
    <span><svg width="14" height="22" viewBox="0 0 14 22"><path d="M11 3L3 11l8 8" fill="none" stroke="#fff" stroke-width="3"/></svg></span>
    <i></i>
    <span><svg width="14" height="22" viewBox="0 0 14 22"><path d="M3 3l8 8-8 8" fill="none" stroke="#fff" stroke-width="3"/></svg></span>
  </div>
</section>

<section>
  <div class="abs about-img" role="img" aria-label="Red calf lying in fresh grass"></div>
  <p class="abs eyebrow about-eyebrow">About Us</p>
  <h2 class="abs heading about-heading">The Heart of Lone<br>Elm Cattle</h2>
  <p class="abs about-text">Sed ut perspiciatis unde omnis iste natus error sit voluptatem accusantium doloremque laudantium, totam rem aperiam, eaque ipsa quae ab illo inventore veritatis et quasi architecto beatae vitae dicta sunt explicabo. Nemo enim ipsam voluptatem quia voluptas sit aspernatur aut odit aut fugit, sed quia consequuntur magni dolores eos qui ratione voluptatem sequi nesciunt. Neque porro quisquam est, qui dolorem ipsum quia dolor sit amet, consectetur, adipisci velit, sed quia non numquam eius modi tempora incidunt ut labore et dolore magnam aliquam quaerat voluptatem.</p>
  <a class="abs btn about-btn">Read More</a>
</section>

<section>
  <div class="abs provide" role="img" aria-label="Misty pasture with grazing cattle"></div>
  <svg class="abs provide-edge" width="1200" height="60" viewBox="0 0 1200 60" preserveAspectRatio="none"><path d="M0 52 L60 40 L140 46 L220 28 L300 38 L380 30 L470 42 L560 26 L650 40 L740 30 L830 44 L920 32 L1010 42 L1100 30 L1200 44 L1200 60 L0 60Z" fill="#fff"/></svg>
  <p class="abs eyebrow center" style="top:1273px">What We Provide</p>
  <h2 class="abs heading center" style="top:1301px">Excellence in Every Sale</h2>
  <div class="abs card" style="left:111px;background:linear-gradient(180deg,#6b5a3a,#2d241b 55%,#b09660)" role="img" aria-label="Black and brown cattle in dry grassland"></div>
  <div class="abs card" style="left:449px;background:linear-gradient(180deg,#c0283a 0%,#1f1b1a 40%,#d9b58a 100%)" role="img" aria-label="Black bull charging across an arena"></div>
  <div class="abs card" style="left:785px;background:linear-gradient(180deg,#3f5a34,#6f8f50 50%,#5e8a3e)" role="img" aria-label="Black and white dairy cow in a green field"></div>
  <div class="abs pill" style="left:144px">Cattle</div>
  <div class="abs pill" style="left:481px">Bulls</div>
  <div class="abs pill" style="left:817px">Cows</div>
</section>

<section>
  <p class="abs eyebrow center" style="top:1937px">Clients Testimonials</p>
  <h2 class="abs heading center" style="top:1965px">What Our Clients Are Saying</h2>
  <div class="abs avatar" role="img" aria-label="Portrait of client"></div>
  <svg class="abs" style="left:111px;top:2212px" width="87" height="70" viewBox="0 0 87 70"><path d="M3 3h35v30l-18 34h-9l8-22H3z M47 3h35v30l-18 34h-9l8-22H47z" fill="none" stroke="#5b4229" stroke-width="3.5" stroke-linejoin="round"/></svg>
  <svg class="abs" style="left:1002px;top:2212px" width="87" height="70" viewBox="0 0 87 70"><path d="M84 67H49V37l18-34h9l-8 22h16z M40 67H5V37l18-34h9l-8 22h16z" fill="none" stroke="#5b4229" stroke-width="3.5" stroke-linejoin="round"/></svg>
  <p class="abs quote-text">Lorem ipsum dolor sit amet, consectetur adipiscing elit, sed do eiusmod tempor incididunt ut labore et dolore magna aliqua. Quis ipsum suspendisse ultrices gravida. Risus commodo viverra maecenas accumsan lacus vel facilisis.</p>
  <p class="abs center client-name">Dale Harmon</p>
  <p class="abs center client-role">Client</p>
  <div class="abs dots"><i></i><i class="on"></i><i></i><i></i></div>
</section>

<footer class="abs site-footer"></footer>
<p class="abs center footer-brand">Lone Elm Cattle</p>
<nav class="abs center footer-nav"><span>Home</span><span>About Us</span><span>Cattle Sales</span><span>Bulls</span><span>Cows</span><span>Gallery</span><span>Contact Us</span></nav>
<div class="abs footer-rule"></div>
<p class="abs center copyright">Copyright © 2025 Lone Elm Cattle. All rights reserved.</p>
</body>
</html>
```